Exhibition/ Conference Booth Design.

To design a background for our booth at an upcoming conference incorporating our logo. We're a market leader in the automation industry for lead-acid batteries. This includes UPS, automobiles, reserve power and traction. The design could be as simple as incorporating our logo into a design to fit our booth that shows we're forward-thinking, innovative future thinking or going into more detail about the different usages for lead-acid batteries.

*Market Leader
*R&D

Company Profile -

KWR is a market-leading supplier of Assembly and Plate Manufacturing equipment that is dedicated to helping businesses of all sizes thrive in today's ever-changing world. With our comprehensive range of products and services, our customer-centric approach, and our commitment to innovation, we are a proven, trusted partner for companies across the globe.

At KWR we are committed to our customers' success. That's why we work closely with them to understand their unique requirements, goals, and challenges, and tailor our solutions to meet their specific needs.

Innovation is at the heart of everything we do at KWR. We invest heavily in research and development to stay ahead of the curve, and we regularly introduce new features, upgrades, and solutions that anticipate our customers' evolving needs. Our commitment to innovation has earned us a reputation as a leader in the industry, and we are constantly exploring new technologies and trends to help our customers succeed.

Industry/Entity Type

Automation - Lead Acid - Engineering

Requirements
Must have
• Our Logo
Nice to have
• Hi All, some good potentials here but I’m wondering if I could update the brief to be more ‘green’ eco friendly - Incorporting where we use Lead Acid batteries. i.e Energy storage, reserve power, automobiles, traction wind/solar and the fact lead acid is widely recyclable. It would be good to see if any of you have some ideas of how to incorporate the logo into this also. Possibly doing something different with the logo colours also.

```html
<!DOCTYPE html>
<html lang="en">
<head>
<meta charset="utf-8">
<title>KWR Engineering – Booth Panel</title>
<link rel="stylesheet" href="https://fonts.googleapis.com/css2?family=Oswald:wght@500;600;700&display=swap">
<style>
  :root {
    --brand-red: #e6332f;
    --brand-red-deep: #d22a2a;
    --brand-blue: #1f5aa6;
    --brand-navy: #15306b;
    --paper: #ffffff;
    --photo-light: #b9c0c8;
    --photo-mid: #7f8a98;
    --photo-dark: #3f4b60;
    --stage: #e9e9ea;
  }
  * { margin: 0; padding: 0; box-sizing: border-box; }
  html, body {
    width: 1200px;
    height: 1200px;
    overflow: hidden;
    background: var(--stage);
  }
  .booth-panel {
    position: relative;
    width: 1200px;
    height: 1200px;
    background: var(--paper);
    overflow: hidden;
    font-family: "Oswald", "Arial Narrow", sans-serif;
  }
  .panel-shapes {
    position: absolute;
    inset: 0;
    width: 1200px;
    height: 1200px;
  }
  .brand-lockup {
    position: absolute;
    top: 58px;
    right: 64px;
    display: flex;
    align-items: center;
    gap: 18px;
    color: var(--brand-blue);
    font-weight: 700;
  }
  .brand-lockup__mark {
    width: 22px;
    height: 22px;
    background: var(--brand-blue);
  }
  .brand-lockup__name {
    display: flex;
    flex-direction: column;
    align-items: center;
    line-height: 1;
  }
  .brand-lockup__word {
    font-size: 104px;
    letter-spacing: 4px;
  }
  .brand-lockup__sub {
    font-size: 30px;
    letter-spacing: 3px;
    margin-top: 6px;
  }
  .headline {
    position: absolute;
    right: 71px;
    top: 700px;
    text-align: right;
    color: var(--paper);
    line-height: 0.96;
    font-weight: 600;
  }
  .headline__line {
    display: block;
    white-space: nowrap;
  }
  .headline__line--soft {
    font-size: 72px;
    letter-spacing: 0.5px;
  }
  .headline__line--loud {
    font-size: 90px;
    text-transform: uppercase;
    letter-spacing: 0.5px;
  }
</style>
</head>
<body>
  <main class="booth-panel">
    <svg class="panel-shapes" viewBox="0 0 784 784" xmlns="http://www.w3.org/2000/svg">
      <defs>
        <linearGradient id="factoryTones" x1="0" y1="0" x2="1" y2="1">
          <stop offset="0" stop-color="var(--photo-light)"/>
          <stop offset="0.55" stop-color="var(--photo-mid)"/>
          <stop offset="1" stop-color="var(--photo-dark)"/>
        </linearGradient>
        <linearGradient id="redWash" x1="0" y1="0" x2="1" y2="1">
          <stop offset="0" stop-color="var(--brand-red)"/>
          <stop offset="1" stop-color="var(--brand-red-deep)"/>
        </linearGradient>
      </defs>

      <path class="factory-photo" role="img"
            aria-label="Photo of engineers working at assembly stations on a battery equipment factory floor"
            d="M0 0 H412 L605 230 L292 598 Q280 612 262 612 L222 612 Q205 612 192 627 L0 440 Z"
            fill="url(#factoryTones)"/>

      <path class="accent-triangle accent-triangle--upper"
            d="M0 218 L84 305 L0 392 Z" fill="var(--brand-blue)" opacity="0.55"/>
      <path class="accent-triangle accent-triangle--lower"
            d="M0 467 L77 542 L0 617 Z" fill="var(--brand-blue)"/>

      <path class="red-field" role="img"
            aria-label="Red tinted photo of a smiling engineer at a workstation"
            d="M612 232 H784 V784 H352 L276 678 Q266 662 280 648 Z"
            fill="url(#redWash)"/>

      <rect class="accent-diamond" x="590" y="190" width="84" height="84" rx="14"
            transform="rotate(45 632 232)" fill="var(--brand-blue)" opacity="0.85"/>

      <rect class="accent-bar" x="114" y="692" width="206" height="37" fill="var(--brand-blue)"/>
      <rect class="accent-block" x="332" y="692" width="60" height="37" fill="var(--paper)"/>
    </svg>

    <div class="brand-lockup">
      <span class="brand-lockup__mark"></span>
      <span class="brand-lockup__name">
        <span class="brand-lockup__word">KWR</span>
        <span class="brand-lockup__sub">ENGINEERING</span>
      </span>
    </div>

    <h1 class="headline">
      <span class="headline__line headline__line--soft">The best speed,</span>
      <span class="headline__line headline__line--loud">Maximum</span>
      <span class="headline__line headline__line--soft">efficiency and</span>
      <span class="headline__line headline__line--loud">Ultimate</span>
      <span class="headline__line headline__line--loud">Output</span>
    </h1>
  </main>
</body>
</html>
```